I need a fresh looking, exciting and loaded design for Full service Restaurant

We need a web design for our restaurant, which offers full service Pakistani and Indian food in PA, USA. Design should be elegant, simplified so customers can navigate easily and order food online for catering as well as delivery. We need loads of pictures and room to grow. I already have a web address via tenvorahost.com. It should include SSL and e-commerce for ordering food.
Be original and be creative and make it a fun site :)

```html
<!DOCTYPE html>
<html lang="en">
<head>
<meta charset="utf-8">
<title>Saffron Courtyard – Pakistani &amp; Indian Restaurant</title>
<link rel="stylesheet" href="https://fonts.googleapis.com/css2?family=Great+Vibes&family=Open+Sans:wght@400;600;700&display=swap">
<style>
:root{
  --red:#c8161d;
  --red-dark:#a10f14;
  --green:#2f6b12;
  --ink:#333333;
  --muted:#555555;
  --white:#ffffff;
  --nav-bg:rgba(40,30,25,.45);
  --caption-bg:rgba(60,50,45,.35);
  --footer:#262626;
  --gold:#c9b27a;
  --shelf:#b07a4e;
}
*{box-sizing:border-box;margin:0;padding:0}
html,body{width:1200px;height:2264px;overflow:hidden}
body{position:relative;background:var(--white);font-family:"Open Sans",Arial,sans-serif;color:var(--ink)}
.abs{position:absolute}
.script{font-family:"Great Vibes",cursive;font-weight:400}

/* Hero */
.hero{left:0;top:0;width:1200px;height:589px;overflow:hidden;
  background:linear-gradient(100deg,#8a6a55 0%,#e9e6e0 18%,#f4f2ee 45%,#e8e2d8 60%,#e06a26 78%,#c84c1c 90%,#6b4a36 100%);
  box-shadow:0 10px 18px rgba(0,0,0,.25)}
.hero-photo{position:absolute;inset:0}
.topbar{left:0;top:0;width:1200px;height:115px;background:var(--nav-bg)}
.brand{left:98px;top:44px;font-size:26px;font-weight:700;color:var(--red);white-space:nowrap}
.brand-mark{display:inline-block;width:14px;height:14px;background:var(--green);border-radius:50%;margin-right:8px;vertical-align:middle}
.main-nav{left:0;top:54px;width:1200px;height:20px}
.main-nav a{position:absolute;color:var(--white);font-size:13px;text-decoration:none;text-transform:uppercase;transform:translateX(-50%);white-space:nowrap}
.search-btn{left:1055px;top:42px;width:42px;height:34px;background:var(--red);border-radius:2px}
.slide-arrow{top:281px;width:20px;height:20px}
.caption{left:0;top:385px;width:871px;height:204px;background:var(--caption-bg)}
.caption p{position:absolute;left:98px;top:38px;color:var(--white);font-size:47px;line-height:68px;white-space:nowrap}

/* About */
.section-title{transform:translateX(-50%);white-space:nowrap;font-size:41px;color:var(--green)}
.ornament{height:8px;width:70px;background:linear-gradient(90deg,transparent,var(--gold),transparent)}
.about-text{left:104px;top:714px;width:492px;text-align:center;font-size:11px;line-height:23px;color:var(--muted)}
.btn{background:linear-gradient(#dd2a2a,var(--red-dark));color:var(--white);text-align:center;border-radius:3px;box-shadow:0 2px 3px rgba(0,0,0,.3)}
.btn-more{left:278px;top:833px;width:136px;height:41px;line-height:41px;font-size:16px;font-weight:600}
.frame{border:1px solid #d8d8d8;padding:5px;background:var(--white);box-shadow:0 1px 3px rgba(0,0,0,.08)}
.frame .photo{width:100%;height:100%}

/* Red band */
.promo{left:0;top:946px;width:1200px;height:251px;
  background:radial-gradient(ellipse at 30% 60%,#c8322a,#a8141a 60%,#8e1014)}
.promo .dash{left:0;width:1200px;border-top:1px dashed rgba(255,255,255,.55)}
.promo-title{left:600px;top:40px;transform:translateX(-50%);white-space:nowrap;font-size:54px;color:var(--white)}
.promo-text{left:0;top:116px;width:1200px;text-align:center;color:var(--white);font-size:25.5px;font-weight:600;line-height:39px}

/* Services */
.service .frame{width:151px;height:133px}
.service h3{position:absolute;left:177px;top:5px;font-size:17px;font-weight:600;color:var(--green);white-space:nowrap}
.service h3.dark{color:var(--ink)}
.service p{position:absolute;left:177px;top:37px;width:290px;font-size:11.5px;line-height:21px;color:var(--muted)}
.service .btn{position:absolute;left:178px;top:95px;width:107px;height:33px;line-height:33px;font-size:13px;font-weight:600}
.chili-area{left:70px;top:1318px;width:64px;height:30px;background:linear-gradient(90deg,rgba(200,22,29,.35),rgba(47,107,18,.25))}

/* Popular foods */
.popular{left:0;top:1732px;width:1200px;height:414px;
  background:linear-gradient(90deg,#231810,#3a2a1e 30%,#2e2117 55%,#3b2a1d 80%,#221710)}
.popular .dash{left:0;top:12px;width:1200px;border-top:1px dashed rgba(255,255,255,.35)}
.popular-title{left:600px;top:54px;transform:translateX(-50%);white-space:nowrap;font-size:46px;color:var(--white)}
.dish{width:300px}
.dish .food-photo{position:absolute;left:50px;top:0;width:200px;height:138px}
.dish .shelf{position:absolute;left:0;top:138px;width:300px;height:31px;background:linear-gradient(#c99066,var(--shelf) 60%,#7d5234);box-shadow:0 6px 8px rgba(0,0,0,.5)}
.dish span{position:absolute;left:0;top:191px;width:300px;text-align:center;color:var(--white);font-size:18px;font-weight:600}

/* Footer */
.footer{left:0;top:2146px;width:1200px;height:118px;background:var(--footer)}
.footer .brand{left:98px;top:42px;color:var(--white);font-size:22px}
.footer .divider{left:342px;top:0;width:1px;height:118px;background:#3d3d3d}
.footer-nav a{position:absolute;top:41px;color:#cfcfcf;font-size:12px;text-decoration:none;text-transform:uppercase;transform:translateX(-50%)}
.footer-nav i{position:absolute;top:47px;width:5px;height:5px;border-radius:50%;background:#cfcfcf}
.copyright{left:342px;top:78px;width:780px;text-align:center;color:#999;font-size:12px}
</style>
</head>
<body>

<header class="abs hero">
  <div class="hero-photo" role="img" aria-label="Photo of basmati rice with green peas and carrots on a plate"></div>
  <div class="abs topbar"></div>
  <div class="abs brand"><span class="brand-mark"></span>Saffron Courtyard</div>
  <nav class="abs main-nav">
    <a href="#" style="left:445px">Home</a>
    <a href="#" style="left:566px">About Us</a>
    <a href="#" style="left:709px">Our Services</a>
    <a href="#" style="left:821px">Dishes</a>
    <a href="#" style="left:970px">Contact Us</a>
  </nav>
  <div class="abs search-btn">
    <svg width="42" height="34" viewBox="0 0 42 34"><circle cx="23" cy="15" r="5" fill="none" stroke="#fff" stroke-width="2.4"/><line x1="19" y1="19" x2="14" y2="24" stroke="#fff" stroke-width="3" stroke-linecap="round"/></svg>
  </div>
  <svg class="abs slide-arrow" style="left:42px" viewBox="0 0 20 20"><polyline points="13,3 6,10 13,17" fill="none" stroke="#fff" stroke-width="2.5"/></svg>
  <svg class="abs slide-arrow" style="left:1135px" viewBox="0 0 20 20"><polyline points="7,3 14,10 7,17" fill="none" stroke="#fff" stroke-width="2.5"/></svg>
  <div class="abs caption"><p class="script">We offer full service Pakistani and Indian food<br>in Philadelphia, USA</p></div>
</header>

<section class="about">
  <div class="abs ornament" style="left:145px;top:669px" role="img" aria-label="Small ornament"></div>
  <h2 class="abs script section-title" style="left:348px;top:642px">Little info about us</h2>
  <div class="abs ornament" style="left:480px;top:669px" role="img" aria-label="Small ornament"></div>
  <p class="abs about-text">Ne iuvaret comprehensam usu. Solet mediocritatem vis cu, mea diam alia dolore ne. Te his soleat equidem eloquentiam, vel ut discere inermis partiendo, cu possim gubergren mea. Idque delicata his ea. Vix ex qualisque periculis, id sit dicta dolorem indoctum. Dicta dissentiet no mea. Quot justo fabellas nam id.</p>
  <div class="abs btn btn-more">More Info</div>
  <div class="abs frame" style="left:641px;top:638px;width:216px;height:256px">
    <div class="photo" role="img" aria-label="Photo of vegetable biryani with cashews" style="background:linear-gradient(160deg,#e9dcc2,#c98d4f 55%,#8a5a2c)"></div>
  </div>
  <div class="abs frame" style="left:882px;top:638px;width:216px;height:256px">
    <div class="photo" role="img" aria-label="Photo of wooden spoons holding spices" style="background:linear-gradient(160deg,#8a5e38,#b88a52 50%,#6a4427)"></div>
  </div>
</section>

<section class="abs promo">
  <div class="abs" style="inset:0" role="img" aria-label="Red tinted photo of spices and wooden spoons"></div>
  <div class="abs dash" style="top:14px"></div>
  <div class="abs dash" style="top:237px"></div>
  <h2 class="abs script promo-title">Ne iuvaret comprehensam usu ! ! !</h2>
  <p class="abs promo-text">Pro stet electram .Mei in agam qualisque. Et est ullum debet.<br>Sit et soleat fastidii iudicabit, ut errem</p>
</section>

<section class="services">
  <div class="abs ornament" style="left:378px;top:1267px" role="img" aria-label="Small ornament"></div>
  <h2 class="abs script section-title" style="left:600px;top:1240px">Our Main Services</h2>
  <div class="abs ornament" style="left:752px;top:1267px" role="img" aria-label="Small ornament"></div>
  <div class="abs chili-area" role="img" aria-label="Decorative red chili peppers"></div>

  <article class="abs service" style="left:98px;top:1348px">
    <div class="frame"><div class="photo" role="img" aria-label="Photo of seekh kebabs" style="background:linear-gradient(160deg,#c9a27a,#7a3e20 50%,#5d8a2e)"></div></div>
    <h3>Ne iuvaret comprehensam</h3>
    <p>Ut pro stet electram. Mei in agam qualisque. Et est ullum debet. Sit et soleat fastidii iudicabit.</p>
    <div class="btn">Read More</div>
  </article>
  <article class="abs service" style="left:643px;top:1348px">
    <div class="frame"><div class="photo" role="img" aria-label="Photo of chicken curry" style="background:linear-gradient(160deg,#6e2a12,#d2541e 50%,#a8351a)"></div></div>
    <h3 class="dark">Mea mucius fierent</h3>
    <p>Ut pro stet electram. Mei in agam qualisque. Et est ullum debet. Sit et soleat fastidii iudicabit.</p>
    <div class="btn">Read More</div>
  </article>
  <article class="abs service" style="left:98px;top:1545px">
    <div class="frame"><div class="photo" role="img" aria-label="Photo of fried pakoras" style="background:linear-gradient(160deg,#f2e6cf,#d98a2a 50%,#b5611a)"></div></div>
    <h3 class="dark">Et est ullum debet</h3>
    <p>Ut pro stet electram. Mei in agam qualisque. Et est ullum debet. Sit et soleat fastidii iudicabit.</p>
    <div class="btn">Read More</div>
  </article>
  <article class="abs service" style="left:643px;top:1545px">
    <div class="frame"><div class="photo" role="img" aria-label="Photo of bowls of spices and vegetables" style="background:linear-gradient(160deg,#2f5a1a,#c9892f 45%,#b8321c 75%,#2d4a16)"></div></div>
    <h3 class="dark">Ne iuvaret comprehensam</h3>
    <p>Ut pro stet electram. Mei in agam qualisque. Et est ullum debet. Sit et soleat fastidii iudicabit.</p>
    <div class="btn">Read More</div>
  </article>
</section>

<section class="abs popular">
  <div class="abs" style="inset:0" role="img" aria-label="Dark photo of spoons filled with spices"></div>
  <div class="abs dash"></div>
  <h2 class="abs script popular-title">Our Popular Foods</h2>
  <div class="abs dish" style="left:99px;top:147px">
    <div class="food-photo" role="img" aria-label="Photo of chana masala in a white bowl" style="background:linear-gradient(180deg,rgba(216,96,34,.55),rgba(200,80,30,.8))"></div>
    <div class="shelf"></div>
    <span>Iuvaret comprehensam</span>
  </div>
  <div class="abs dish" style="left:449px;top:147px">
    <div class="food-photo" role="img" aria-label="Photo of curry in a copper karahi" style="background:linear-gradient(180deg,rgba(200,110,50,.55),rgba(180,80,30,.8))"></div>
    <div class="shelf"></div>
    <span>Solet mediocritatem</span>
  </div>
  <div class="abs dish" style="left:801px;top:147px">
    <div class="food-photo" role="img" aria-label="Photo of vegetable pulao in a clay bowl" style="background:linear-gradient(180deg,rgba(230,220,200,.5),rgba(170,80,40,.8))"></div>
    <div class="shelf"></div>
    <span>Diam alia dolore ne</span>
  </div>
</section>

<footer class="abs footer">
  <div class="abs brand"><span class="brand-mark" style="background:var(--white)"></span>Saffron Courtyard</div>
  <div class="abs divider"></div>
  <nav class="footer-nav">
    <a href="#" style="left:421px">Home</a><i style="left:474px"></i>
    <a href="#" style="left:531px">About</a><i style="left:588px"></i>
    <a href="#" style="left:653px">Services</a><i style="left:713px"></i>
    <a href="#" style="left:777px">Clients</a><i style="left:840px"></i>
    <a href="#" style="left:905px">Carrees</a><i style="left:966px"></i>
    <a href="#" style="left:1031px">Contact</a>
  </nav>
  <p class="abs copyright">All Rights Reserved . copyrights2016@companyname.com</p>
</footer>

</body>
</html>
```